Poster to advertise velquin and dermal fillers

I want a poster to put up in beauty salons to advertise velquin and dermal fillers.
Velquin is used to reduce fine lines and wrinkles around the eyes and across the forehead, between the eyebrows and dermal fillers are used to add volume under the skin where it begins to sag.
The products are mainly used by women.
I am an advanced aesthetic nurse and a member of the Harwell Guild of cosmetic nurses.
I want the poster to be quite feminine with soft colours, eye catching and not too busy, not too much information. It may go in the window of the salon to attract passing trade.
I want it to state that these treatments are available at the particular salon by an advanced trained nurse. "Please ask for further details or to arrange a consultation". etc
My company is called plum Willow

Target Market(s)

Mainly women

Industry/Entity Type

Nurse

Requirements
Should not have
• harsh colours, no jokes

```html
<!DOCTYPE html>
<html lang="en">
<head>
<meta charset="utf-8">
<title>Plum Willow – Velquin &amp; Dermal Fillers</title>
<link rel="stylesheet" href="https://fonts.googleapis.com/css2?family=Tinos:wght@700&display=swap">
<style>
  :root {
    --ink: #0d0d0d;
    --soft-grey: #7c7878;
    --blush: #f1c8ec;
    --plum: #8a1f6b;
    --sky: #cfe6f5;
    --skin: #f3ece9;
    --skin-deep: #e9dcd8;
  }
  * { margin: 0; padding: 0; box-sizing: border-box; }
  html, body { width: 848px; height: 1200px; overflow: hidden; background: #fff; }
  .poster {
    position: relative;
    width: 848px;
    height: 1200px;
    overflow: hidden;
    font-family: "Tinos", "Times New Roman", serif;
    font-weight: 700;
    color: var(--ink);
  }
  .backdrop {
    position: absolute; inset: 0;
    background:
      radial-gradient(ellipse 330px 520px at 560px 560px, var(--skin-deep) 0%, var(--skin) 60%, rgba(243,236,233,0) 100%),
      linear-gradient(90deg, var(--sky) 0%, #e3eff7 35%, var(--skin) 70%, #f6f2f1 100%);
  }
  .title {
    position: absolute; top: 18px; left: 0; width: 100%;
    text-align: center; font-size: 116px; line-height: 1;
    letter-spacing: 1px;
  }
  .tagline {
    position: absolute; top: 186px; left: 0; width: 100%;
    text-align: center; font-size: 44px; line-height: 66px;
    color: var(--soft-grey);
  }
  .treatment { position: absolute; left: 28px; }
  .treatment h2 { font-size: 46px; line-height: 1; }
  .treatment p { font-size: 25px; line-height: 1.2; margin-top: 8px; }
  .treatment--fillers { top: 358px; }
  .treatment--velquin { top: 522px; }
  .badge {
    position: absolute; border-radius: 50%;
    background: var(--blush);
    display: flex; align-items: center; justify-content: center;
    text-align: center;
  }
  .badge--available {
    left: 572px; top: 356px; width: 252px; height: 252px;
  }
  .badge--available span {
    display: block; font-size: 44px; line-height: 52px;
    transform: rotate(16deg);
  }
  .badge--nurse {
    left: 26px; top: 676px; width: 320px; height: 318px;
  }
  .badge--nurse span {
    display: block; font-size: 22px; line-height: 27px;
    width: 230px; transform: rotate(-8deg);
  }
  .enquiry {
    position: absolute; top: 724px; left: 372px; width: 462px;
    text-align: center; font-size: 44px; line-height: 54px;
    color: var(--soft-grey);
  }
  .contact {
    position: absolute; top: 1092px; left: 42px;
    font-size: 23px; line-height: 32px; color: var(--soft-grey);
  }
  .guild {
    position: absolute; top: 1050px; left: 566px; width: 264px;
    display: flex; align-items: center; gap: 12px;
    color: var(--plum); font-size: 21px; line-height: 25px;
  }
  .guild__mark { flex: none; width: 26px; height: 26px; background: var(--plum); }
</style>
</head>
<body>
<main class="poster">
  <div class="backdrop" role="img" aria-label="Soft-focus portrait of a woman receiving a cosmetic injection treatment"></div>

  <h1 class="title">Plum Willow</h1>
  <p class="tagline">Ever thought of treating yourself<br>to a more youthful apperance?</p>

  <section class="treatment treatment--fillers">
    <h2>DERMAL FILLERS</h2>
    <p>Adds volume under the skin</p>
  </section>

  <section class="treatment treatment--velquin">
    <h2>VELQUIN</h2>
    <p>Reduce fine lines and wrinkles</p>
  </section>

  <div class="badge badge--available"><span>Available<br>Here</span></div>

  <div class="badge badge--nurse">
    <span>All treatments carried out by an advanced trained nurse and member of the harwell guild of cosmetic nurses.</span>
  </div>

  <p class="enquiry">Please ask for<br>further details<br>or to arrange<br>a free consultation.</p>

  <p class="contact">Contact details<br>Website</p>

  <div class="guild">
    <span class="guild__mark"></span>
    <span class="guild__name">Harwell Guild of Cosmetic Nurses</span>
  </div>
</main>
</body>
</html>
```